Strong, modern, clean Business Card design

Looking for a stunning, but CLEAN business card design. While we are a faith-based organization, we do NOT want this to look religious.

Industry/Entity Type

Non-Profit

Contact Information for Business Card

Dale Munroe | Lead Pastor
dale@BrightHarvestHope.org
970-555-0148
PO Box 7316
Millbrook, OR 80571

Font styles to use
Serif
Sans Serif

Requirements
Should not have
• Religious imagery or symbolism

```html
<!DOCTYPE html>
<html lang="en">
<head>
<meta charset="utf-8">
<title>Bright Harvest Church – Business Card</title>
<link rel="stylesheet" href="https://fonts.googleapis.com/css2?family=Crimson+Pro:wght@400;600;700&display=swap">
<style>
  :root {
    --backdrop: #d4d8d9;
    --brand-blue: #48758f;
    --paper: #f6f6f4;
    --ink: #1e2326;
    --white: #ffffff;
  }
  * { box-sizing: border-box; margin: 0; padding: 0; }
  html, body { width: 1200px; height: 1050px; overflow: hidden; }
  body {
    background: var(--backdrop);
    font-family: "Crimson Pro", Georgia, serif;
    display: flex;
    flex-direction: column;
    align-items: center;
    justify-content: center;
    gap: 40px;
  }
  .card {
    width: 840px;
    height: 480px;
    position: relative;
    box-shadow: 0 6px 18px rgba(0,0,0,0.12);
  }
  .card--front {
    background: var(--brand-blue);
    display: flex;
    align-items: center;
    justify-content: center;
  }
  .card--back { background: var(--paper); }

  .wordmark {
    font-family: "Crimson Pro", Georgia, serif;
    font-weight: 600;
    text-transform: uppercase;
    line-height: 1.05;
    display: flex;
    flex-direction: column;
  }
  .wordmark__main { letter-spacing: 0.03em; white-space: nowrap; }
  .wordmark__sub { letter-spacing: 0.6em; font-size: 0.42em; margin-top: 6px; padding-left: 0.9em; white-space: nowrap; }

  .card--front .wordmark { color: var(--white); font-size: 64px; }
  .card--back .wordmark {
    color: var(--brand-blue);
    font-size: 42px;
    position: absolute;
    left: 70px;
    top: 58px;
  }

  .contact {
    position: absolute;
    left: 440px;
    top: 255px;
    color: var(--ink);
    font-size: 21px;
    line-height: 1.3;
  }
  .contact__name {
    font-size: 29px;
    font-weight: 700;
    color: var(--brand-blue);
    margin-bottom: 8px;
    white-space: nowrap;
  }
  .contact__divider { color: var(--brand-blue); font-weight: 400; margin: 0 4px; }
  .contact__role { font-size: 21px; font-weight: 400; color: var(--ink); }
  .contact__line { display: flex; align-items: center; gap: 8px; white-space: nowrap; }
  .contact__icon { width: 14px; height: 14px; flex: none; }
  .contact__line--plain { padding-left: 22px; }
</style>
</head>
<body>
  <section class="card card--front" aria-label="Card front">
    <div class="wordmark">
      <span class="wordmark__main">Bright Harvest</span>
      <span class="wordmark__sub">Church</span>
    </div>
  </section>

  <section class="card card--back" aria-label="Card back">
    <div class="wordmark">
      <span class="wordmark__main">Bright Harvest</span>
      <span class="wordmark__sub">Church</span>
    </div>

    <div class="contact">
      <div class="contact__name">Dale Munroe<span class="contact__divider">|</span><span class="contact__role">Lead Pastor</span></div>
      <div class="contact__line contact__line--plain">PO Box 7316</div>
      <div class="contact__line contact__line--plain">Millbrook, OR 80571</div>
      <div class="contact__line">
        <svg class="contact__icon" viewBox="0 0 16 16" aria-hidden="true">
          <path d="M4 1.5 L6 4.5 L4.8 6 C5.6 8 7.8 10.3 10 11.2 L11.5 10 L14.5 12 L13 14.5 C7.5 14 2 8.5 1.5 3 Z" fill="var(--brand-blue)"/>
        </svg>
        970-555-0148
      </div>
      <div class="contact__line">
        <svg class="contact__icon" viewBox="0 0 16 16" aria-hidden="true">
          <rect x="1" y="3" width="14" height="10" fill="none" stroke="var(--brand-blue)" stroke-width="1.4"/>
          <path d="M1 3 L8 9 L15 3" fill="none" stroke="var(--brand-blue)" stroke-width="1.4"/>
        </svg>
        dale@BrightHarvestHope.org
      </div>
    </div>
  </section>
</body>
</html>
```